Brindle Logistics Business Card Design

We are a trucking and warehousing company. We run freight in the US manly from the Pacific NW to TX and back up the the PNW. We also do warehousing where we store, move, and distribute freight. Looking for a clean and modern design of business card. We would like to look rich and elegant. Attached is our logo.

Industry/Entity Type

Trucking Company

Contact Information for Business Card

Looking for a clean and modern design of business card. We would like to look rich and elegant.

Font styles to use
Sans Serif

Colors

Designer to choose colors to be used in the design.

Requirements
Must have
• logo but it should not dominate the card
Should not have
• logo should not dominate the card

```html
<!DOCTYPE html>
<html lang="en">
<head>
<meta charset="utf-8">
<title>Brindle Logistics Business Card</title>
<link href="https://fonts.googleapis.com/css2?family=Montserrat:wght@600;700&family=Arimo:wght@400&display=swap" rel="stylesheet">
<style>
  :root {
    --backdrop: #2b2b2d;
    --card: #ffffff;
    --ink: #3a3a3c;
    --muted: #55575a;
    --brand: #1a72bd;
    --rule: #9a9c9f;
  }
  * { box-sizing: border-box; margin: 0; padding: 0; }
  html, body { width: 1200px; height: 864px; overflow: hidden; }
  body {
    background: var(--backdrop);
    position: relative;
    font-family: "Arimo", Arial, sans-serif;
    color: var(--ink);
  }
  .card {
    position: absolute;
    left: 300px;
    width: 600px;
    height: 343px;
    background: var(--card);
    border-radius: 26px;
    box-shadow: 0 10px 30px rgba(0,0,0,.45);
  }
  .card-front { top: 50px; }
  .card-back { top: 471px; }

  .wordmark {
    display: flex;
    align-items: center;
    gap: 12px;
    font-family: "Montserrat", sans-serif;
    font-weight: 700;
    color: var(--brand);
    letter-spacing: 0.04em;
    text-transform: uppercase;
    line-height: 1.1;
  }
  .wordmark-dot {
    width: 34px; height: 34px;
    border-radius: 50%;
    background: var(--brand);
    flex: none;
  }
  .card-front .wordmark {
    position: absolute;
    right: 58px;
    top: 150px;
    font-size: 24px;
  }

  .back-layout {
    position: absolute;
    inset: 0;
    display: flex;
    align-items: center;
    justify-content: center;
  }
  .company-side {
    width: 270px;
    display: flex;
    flex-direction: column;
    align-items: flex-end;
    padding-right: 22px;
  }
  .company-side .wordmark { font-size: 19px; }
  .address {
    margin-top: 14px;
    text-align: right;
    font-size: 15px;
    line-height: 1.35;
    color: var(--muted);
  }
  .divider {
    width: 1px;
    height: 134px;
    background: var(--rule);
  }
  .person-side {
    width: 270px;
    padding-left: 22px;
  }
  .person-name {
    font-family: "Montserrat", sans-serif;
    font-weight: 700;
    font-size: 21px;
    letter-spacing: 0.04em;
    text-transform: uppercase;
    color: var(--ink);
  }
  .person-role {
    font-family: "Montserrat", sans-serif;
    font-weight: 700;
    font-size: 14px;
    letter-spacing: 0.05em;
    text-transform: uppercase;
    color: var(--brand);
    margin-bottom: 14px;
  }
  .contact-list { list-style: none; }
  .contact-item {
    display: flex;
    align-items: center;
    gap: 10px;
    font-size: 14px;
    color: var(--muted);
    margin-bottom: 5px;
  }
  .contact-icon { width: 13px; height: 13px; flex: none; fill: var(--brand); }
</style>
</head>
<body>
  <section class="card card-front" aria-label="Card front">
    <div class="wordmark">
      <span class="wordmark-dot"></span>
      <span>Brindle<br>Logistics, LLC</span>
    </div>
  </section>

  <section class="card card-back" aria-label="Card back">
    <div class="back-layout">
      <div class="company-side">
        <div class="wordmark">
          <span class="wordmark-dot"></span>
          <span>Brindle<br>Logistics, LLC</span>
        </div>
        <p class="address">48 Larkspur Road<br>Alder Valley, Westbrook<br>Saskatchewan, S0K 2L7</p>
      </div>
      <div class="divider"></div>
      <div class="person-side">
        <h1 class="person-name">Dana Morrow</h1>
        <p class="person-role">Managing Director</p>
        <ul class="contact-list">
          <li class="contact-item">
            <svg class="contact-icon" viewBox="0 0 24 24" aria-hidden="true"><path d="M6.6 10.8a15.1 15.1 0 0 0 6.6 6.6l2.2-2.2a1 1 0 0 1 1-.25 11.4 11.4 0 0 0 3.6.57 1 1 0 0 1 1 1V20a1 1 0 0 1-1 1A17 17 0 0 1 3 4a1 1 0 0 1 1-1h3.5a1 1 0 0 1 1 1c0 1.25.2 2.45.57 3.57a1 1 0 0 1-.25 1z"/></svg>
            555.014.2280
          </li>
          <li class="contact-item">
            <svg class="contact-icon" viewBox="0 0 24 24" aria-hidden="true"><path d="M2 5h20v14H2z M4 7v.4l8 5.2 8-5.2V7z" fill-rule="evenodd"/></svg>
            info@brindlelogistics.com
          </li>
          <li class="contact-item">
            <svg class="contact-icon" viewBox="0 0 24 24" aria-hidden="true"><path d="M12 2a10 10 0 1 0 0 20 10 10 0 0 0 0-20zm0 2c.9 1.2 1.6 2.6 2 4h-4c.4-1.4 1.1-2.8 2-4zM4.3 14a8 8 0 0 1 0-4h3.4a16 16 0 0 0 0 4zm.8 2h3a14 14 0 0 0 1.3 3.5A8 8 0 0 1 5.1 16zm3-8h-3a8 8 0 0 1 4.3-3.5A14 14 0 0 0 8.1 8zM12 20c-.9-1.2-1.6-2.6-2-4h4c-.4 1.4-1.1 2.8-2 4zm2.3-6H9.7a14 14 0 0 1 0-4h4.6a14 14 0 0 1 0 4zm.3 5.5A14 14 0 0 0 15.9 16h3a8 8 0 0 1-4.3 3.5zm1.7-5.5a16 16 0 0 0 0-4h3.4a8 8 0 0 1 0 4zm-.4-6a14 14 0 0 0-1.3-3.5A8 8 0 0 1 18.9 8z"/></svg>
            www.brindlelogistics.com
          </li>
        </ul>
      </div>
    </div>
  </section>
</body>
</html>
```